nonprofit organization looking for sleek new design

We need a fresh new look for this nonprofit organization, Harbor Lights Family Works, INC (HALIF, Inc.). This organization provides educational, nutritional, dental health, and specialized services to Tidewell children, aiming to support families meeting federal income poverty guidelines. Our mission is clear: "Creating a brighter future for the children and la familia." We focus on child development, family wellness, staff growth, and community partnerships.

```html
<!DOCTYPE html>
<html lang="en">
<head>
<meta charset="utf-8">
<title>Harbor Lights Family Works, INC</title>
<link href="https://fonts.googleapis.com/css2?family=Poppins:wght@400;500;600;700;800&display=swap" rel="stylesheet">
<style>
:root{
  --red:#e3191f;
  --blue:#22409a;
  --navy:#1b2f73;
  --ink:#111111;
  --text:#4a4a4a;
  --pink:#fdeeee;
  --white:#ffffff;
  --grey:#2b2b2b;
}
*{box-sizing:border-box;margin:0;padding:0}
html,body{width:1200px;height:4992px;overflow:hidden}
body{font-family:'Poppins',sans-serif;color:var(--ink);background:var(--white);position:relative}
.abs{position:absolute}
.eyebrow{font-size:17px;letter-spacing:5px;font-weight:500;text-transform:uppercase}
.btn{display:inline-flex;align-items:center;justify-content:center;font-weight:700;font-size:11px;text-transform:uppercase;color:var(--white);border-radius:3px;letter-spacing:.5px}
.btn-red{background:var(--red)}
.btn-blue{background:var(--blue)}

/* hero */
.hero{left:0;top:0;width:1200px;height:667px;background:linear-gradient(100deg,#2a1c16 0%,#4a3226 45%,#7a5a42 70%,#3b2a20 100%)}
.hero-photo{left:0;top:0;width:1200px;height:667px;background:radial-gradient(ellipse at 72% 55%,rgba(190,140,100,.55),rgba(0,0,0,0) 55%)}
.hero-shade{left:0;top:0;width:1200px;height:667px;background:linear-gradient(90deg,rgba(0,0,0,.55),rgba(0,0,0,.05) 60%)}
.brand{left:125px;top:26px;display:flex;align-items:center;gap:8px;color:var(--white);font-weight:700;font-size:15px}
.brand .dot{width:26px;height:26px;border-radius:50%;background:var(--red)}
.nav{left:255px;top:36px;display:flex;gap:30px;font-size:10px;font-weight:600;color:var(--white);text-transform:uppercase}
.nav .on{color:var(--red)}
.donate{left:985px;top:31px;width:88px;height:38px}
.hero-eyebrow{left:125px;top:176px;color:var(--white)}
.hero h1{left:125px;top:205px;color:var(--white);font-size:42px;line-height:44px;font-weight:800;text-transform:uppercase;width:440px}
.hero p{left:125px;top:354px;width:400px;color:var(--white);font-size:13px;line-height:19px}
.join{left:125px;top:443px;width:133px;height:36px}
.watch{left:282px;top:443px;width:228px;height:36px;gap:8px}

/* about */
.impact{left:125px;top:624px;width:425px;height:556px;background:var(--blue);color:var(--white);padding:102px 50px 0 50px}
.impact h2{font-size:24px;line-height:26px;font-weight:700;margin-bottom:22px;width:250px}
.impact p{font-size:12px;line-height:19px;margin-bottom:14px}
.about{left:605px;top:706px;width:475px}
.about h2{font-size:38px;font-weight:700;margin-bottom:14px}
.about p{font-size:12.5px;line-height:19px;color:var(--text);margin-bottom:12px}
.about .btn{width:138px;height:36px;margin-top:14px}

/* services */
.services{left:0;top:1208px;width:1200px;height:806px;background:var(--pink)}
.center{width:1200px;text-align:center;left:0}
.services .eyebrow{top:98px;color:var(--red)}
.services h2{top:126px;font-size:36px;line-height:37px;font-weight:800;text-transform:uppercase}
.services .sub{top:262px;left:300px;width:600px;font-size:12px;line-height:19px;color:var(--text);text-align:center}
.card{top:348px;width:222px;height:270px;background:var(--white);text-align:center;padding:38px 18px 0}
.card svg{width:46px;height:46px}
.card h3{font-size:12px;line-height:18px;font-weight:600;margin:12px 0 14px}
.card p{font-size:11px;line-height:17px;color:var(--text)}
.card a{display:block;margin-top:18px;font-size:11px;font-weight:700;color:var(--blue);text-decoration:underline}
.round{width:40px;height:40px;border-radius:50%;display:flex;align-items:center;justify-content:center}
.round.red{background:var(--red)}

/* causes */
.causes{left:0;top:2014px;width:1200px;height:889px}
.causes .eyebrow{left:125px;top:98px;color:var(--red)}
.causes h2{left:125px;top:128px;font-size:38px;line-height:40px;font-weight:800;text-transform:uppercase;width:400px}
.divider{left:690px;top:128px;width:1px;height:100px;background:#ccc}
.causes .lead{left:722px;top:132px;width:360px;font-size:12.5px;line-height:19px;color:var(--text)}
.cause{top:294px;width:305px}
.cause h3{font-size:15px;font-weight:600;text-transform:uppercase;margin-bottom:16px}
.cause .ph{width:305px;height:200px;position:relative}
.cause .pct{position:absolute;left:90px;top:60px;width:78px;height:78px;border-radius:50%;background:rgba(20,20,20,.75);border:4px solid var(--white);border-right-color:rgba(255,255,255,.3);color:var(--white);display:flex;align-items:center;justify-content:center;font-size:24px;font-weight:700}
.raise{font-size:13px;margin:18px 0 10px;color:var(--text)}
.raise b{color:var(--red);font-weight:600}
.cause p{font-size:11.5px;line-height:17px;color:var(--text)}
.cause .btn{width:137px;height:26px;margin-top:24px;background:var(--navy);border-radius:4px;font-size:10px}
.seeall{left:125px;top:746px;width:172px;height:38px}

/* events */
.events{left:0;top:2903px;width:1200px;height:653px;background:linear-gradient(180deg,#1a1111,#2c1c1c 60%,#140e0e)}
.events .eyebrow{top:92px;color:var(--red)}
.events h2{top:120px;font-size:38px;line-height:40px;font-weight:800;color:var(--white);text-transform:uppercase}
.ev{top:245px;width:464px;height:305px}
.ev .date{position:absolute;left:0;top:0;width:40px;height:44px;background:var(--blue);color:var(--white);font-size:10px;font-weight:700;text-align:center;padding-top:7px;line-height:14px}
.ev .lbl{position:absolute;left:0;bottom:0;width:320px;height:110px;background:var(--blue);color:var(--white);padding:20px 28px}
.ev .lbl h3{font-size:18px;line-height:23px;font-weight:700}
.ev .lbl span{display:block;font-size:10px;margin-top:10px;font-weight:600}
.sq{width:36px;height:36px;background:var(--white);display:flex;align-items:center;justify-content:center}

/* testimonials */
.testi{left:0;top:3556px;width:1200px;height:700px}
.testi .eyebrow{left:135px;top:115px;color:var(--red)}
.testi h2{left:125px;top:140px;font-size:37px;font-weight:800;text-transform:uppercase}
.testi .divider{left:628px;top:105px;height:90px}
.testi .lead{left:742px;top:114px;width:300px;font-size:12.5px;line-height:19px;color:var(--text)}
.tc{top:286px;width:435px;height:186px;padding:56px 38px 0;font-size:12px;line-height:18px}
.tc.blue{background:var(--blue);color:var(--white)}
.tc.white{background:var(--white);color:var(--text);box-shadow:0 2px 18px rgba(0,0,0,.08)}
.tc .q{position:absolute;right:78px;top:-18px;font-size:72px;font-weight:800;color:var(--red);line-height:72px}
.tc .who{position:absolute;right:60px;bottom:34px;font-size:12px;font-weight:700;letter-spacing:2px;text-transform:uppercase}
.tc.white .who{color:var(--ink)}
.av{position:absolute;left:44px;bottom:-26px;width:72px;height:72px;border-radius:50%;border:4px solid var(--white)}
.ring{width:40px;height:40px;border-radius:50%;display:flex;align-items:center;justify-content:center}

/* footer */
.footer{left:0;top:4417px;width:1200px;height:575px;background:#0a0a0a}
.news{left:120px;top:4245px;width:955px;height:270px;background:var(--blue);color:var(--white)}
.news small{position:absolute;left:80px;top:88px;font-size:14px}
.news h2{position:absolute;left:80px;top:112px;font-size:38px;line-height:44px;font-weight:500}
.field{position:absolute;left:410px;width:465px;height:44px;background:var(--white);border-radius:3px;font-size:11px;color:#777;padding:14px 18px}
.send{position:absolute;right:0;top:0;width:44px;height:44px;background:#3d7be0;display:flex;align-items:center;justify-content:center;border-radius:0 3px 3px 0}
.foot-brand{left:0;width:1200px;top:4600px;display:flex;justify-content:center;align-items:center;gap:10px;color:var(--white);font-weight:700;font-size:22px}
.foot-brand .dot{width:34px;height:34px;border-radius:50%;background:var(--red)}
.socials{left:0;width:1200px;top:4700px;display:flex;justify-content:center;gap:28px}
.socials span{width:56px;height:56px;border-radius:50%;background:var(--grey);display:block}
.foot-nav{left:125px;top:4792px;width:950px;height:56px;background:var(--grey);display:flex;justify-content:space-around;align-items:center;font-size:10px;font-weight:600;color:var(--white);text-transform:uppercase;padding:0 40px}
.copy{left:0;width:1200px;top:4950px;text-align:center;color:var(--white);font-size:13px}
</style>
</head>
<body>

<section class="abs hero">
  <div class="abs hero-photo" role="img" aria-label="Photo of a young boy holding a small wooden house model outdoors"></div>
  <div class="abs hero-shade"></div>
  <div class="abs brand"><span class="dot"></span>HALIF, Inc.</div>
  <nav class="abs nav"><span class="on">Home</span><span>Services</span><span>Administration</span><span>School Readiness</span><span>Employment</span><span>About Us</span><span>PFR - Apply Now</span></nav>
  <span class="abs btn btn-red donate">Donate</span>
  <div class="abs eyebrow hero-eyebrow">Explore Our</div>
  <h1 class="abs">Nonprofit Initiatives for a Brighter Future.</h1>
  <p class="abs">Lorem Ipsum is simply dummy text of the printing and typesetting industry. Lorem Ipsum has been the industry's standard dum</p>
  <span class="abs btn btn-red join">Join Us</span>
  <span class="abs btn btn-blue watch"><svg width="12" height="12" viewBox="0 0 12 12"><path d="M2 1l9 5-9 5z" fill="#fff"/></svg>Watch what we've done</span>
</section>

<div class="abs impact">
  <h2>Make A Lasting Impact On Lives In Need</h2>
  <p>Lorem Ipsum is simply dummy text of the printing and typesetting industry. Lorem Ipsum has been the industry's standard dummy text ever since the 1500s, when an unknown printer took a galley of type and scrambled it to make a type specimen book.</p>
  <p>It has survived not only five centuries, but also the leap into electronic typesetting, remaining essentially unchanged. It was popularised in the 1960s with the release of Letraset sheets containing Lorem Ipsum passages, and more recently with desktop publishing software including versions of Lorem Ipsum. 1960s with the release of Letraset sheets containing.</p>
</div>
<div class="abs about">
  <h2>ABOUT US</h2>
  <p>The Harbor Lights Family Works, Incorporated (HALIF, Inc.) Tidewell Early Start program was established in March 1991 and is a non-profit organization in IRS Code Section 501(c) 3. The program is funded by the State Family Services Council regional office in Brookhaven, and it operates four grants: Tidewell, Early Tidewell, Bridge, and Seedling. The service area covers birth through four (4) years of age. Tidewell children receive services that include educational, nutritional, health, transitional, and special services. One of the criteria for receiving Tidewell services is that the families must meet federal income poverty guidelines.</p>
  <p>The mission of HALIF, Inc. is "Creating a brighter future for the children and la familia." We work to enhance the development of young children; promote healthy family functioning; provide for staff development and establish partners among the Community.</p>
  <span class="btn btn-red">Get Involved</span>
</div>

<section class="abs services">
  <div class="abs center eyebrow">Our Services</div>
  <h2 class="abs center">Pave the way for a brighter,<br>more compassionate<br>world.</h2>
  <p class="abs sub">HALIF, Inc. is always interested in taking applications for pregnant women, children and children with Disabilities Ages 0-4 Years old.</p>
  <div class="abs card" style="left:125px">
    <svg viewBox="0 0 46 46"><path d="M23 40C10 30 4 23 4 15a9 9 0 0 1 19-4 9 9 0 0 1 19 4c0 8-6 15-19 25z" fill="#22409a"/><path d="M8 22h9l3-6 4 10 3-4h11" stroke="#fff" stroke-width="2.5" fill="none"/></svg>
    <h3>Health and Nutritional Assessments</h3>
    <p>Lorem Ipsum is simply dummy text of the printing and typeset</p>
    <a>READ MORE</a>
  </div>
  <div class="abs card" style="left:367px">
    <svg viewBox="0 0 46 46"><path d="M8 10c4-4 10-3 15 0 5-3 11-4 15 0 3 5 1 12-1 18l-3 14h-4l-3-12h-8l-3 12h-4L9 28C7 22 5 15 8 10z" fill="#22409a"/><circle cx="37" cy="9" r="7" fill="#22409a" stroke="#fff" stroke-width="2"/><path d="M37 5v8M33 9h8" stroke="#fff" stroke-width="2"/></svg>
    <h3>Medical and Dental<br>Follow-Ups</h3>
    <p>Lorem Ipsum is simply dummy text of the printing and typeset</p>
    <a>READ MORE</a>
  </div>
  <div class="abs card" style="left:608px">
    <svg viewBox="0 0 46 46"><circle cx="22" cy="8" r="5" fill="#22409a"/><path d="M17 15h9l2 8c6 2 7 8 3 11l-1 9h-12l-1-14c-2-4 0-10 0-14z" fill="#22409a"/></svg>
    <h3>Pre and Post Natal Education for Pregnant Women</h3>
    <p>Lorem Ipsum is simply dummy text of the printing and typeset</p>
    <a>READ MORE</a>
  </div>
  <div class="abs card" style="left:850px">
    <svg viewBox="0 0 46 46"><circle cx="23" cy="24" r="13" fill="none" stroke="#22409a" stroke-width="3"/><circle cx="23" cy="24" r="7" fill="#22409a"/><path d="M5 8v10M3 8v6M7 8v6M5 18v20M41 8c-4 3-4 10 0 12v18" stroke="#22409a" stroke-width="2.5" fill="none"/></svg>
    <h3>Nutritional Meals &amp;<br>Snacks</h3>
    <p>Lorem Ipsum is simply dummy text of the printing and typeset</p>
    <a>READ MORE</a>
  </div>
  <div class="abs round red" style="left:546px;top:668px"><svg width="16" height="16" viewBox="0 0 16 16"><path d="M14 8H3M7 3L2 8l5 5" stroke="#fff" stroke-width="2" fill="none"/></svg></div>
  <div class="abs round red" style="left:612px;top:668px"><svg width="16" height="16" viewBox="0 0 16 16"><path d="M2 8h11M9 3l5 5-5 5" stroke="#fff" stroke-width="2" fill="none"/></svg></div>
</section>

<section class="abs causes">
  <div class="abs eyebrow">See Our Causes</div>
  <h2 class="abs">You can help lots of people by donating little</h2>
  <div class="abs divider"></div>
  <p class="abs lead">Lorem Ipsum is simply dummy text of the printing and typesetting industry. Lorem Ipsum has been the industry's standard dummy text ever since the 1500s, when an unknown printer took a gal</p>
  <div class="abs cause" style="left:125px">
    <h3>Ending Child Marriage</h3>
    <div class="ph" role="img" aria-label="Photo of a young girl in a doorway with a person walking away" style="background:linear-gradient(120deg,#6b6a68,#2e2c2a 55%,#8d8a84)"><div class="pct">1%</div></div>
    <div class="raise">Raised: <b>$1,000</b> / Goals: <b>$10,0000</b></div>
    <p>Lorem Ipsum is simply dummy text of the printing and typeset text of the printing and typeset</p>
    <span class="btn">Campaign Ended</span>
  </div>
  <div class="abs cause" style="left:447px">
    <h3>Civil and Political Rights</h3>
    <div class="ph" role="img" aria-label="Photo of a crowd of protesters raising their fists" style="background:linear-gradient(160deg,#9a9894,#3b3936 60%,#1f1d1b)"><div class="pct">4%</div></div>
    <div class="raise">Raised: <b>$1,000</b> / Goals: <b>$10,0000</b></div>
    <p>Lorem Ipsum is simply dummy text of the printing and typeset text of the printing and typeset</p>
    <span class="btn">Campaign Ended</span>
  </div>
  <div class="abs cause" style="left:770px">
    <h3>Elderly Person</h3>
    <div class="ph" role="img" aria-label="Photo of an elderly man seated indoors" style="background:linear-gradient(120deg,#8e8c88,#5d5a55 50%,#c2bfb8)"><div class="pct">5%</div></div>
    <div class="raise">Raised: <b>$1,000</b> / Goals: <b>$10,0000</b></div>
    <p>Lorem Ipsum is simply dummy text of the printing and typeset text of the printing and typeset</p>
    <span class="btn">Campaign Ended</span>
  </div>
  <span class="abs btn btn-red seeall">See All Causes</span>
</section>

<section class="abs events">
  <div class="abs center eyebrow">Our Events</div>
  <h2 class="abs center">Unite with us at<br>events for a cause</h2>
  <div class="abs ev" style="left:125px;background:linear-gradient(120deg,#c9a98e,#8a6a55 50%,#4d3a30)" role="img" aria-label="Photo of a little girl playing outdoors in autumn">
    <div class="date">21<br>MAR</div>
    <div class="lbl"><h3>Lorem Ipsum Is Simply Dummy Text Of The Printing</h3><span>READ MORE ⟶</span></div>
  </div>
  <div class="abs ev" style="left:611px;background:linear-gradient(120deg,#8fa26a,#5e7444 50%,#3c4a2e)" role="img" aria-label="Photo of a girl looking through a magnifying glass outdoors">
    <div class="date">21<br>MAR</div>
    <div class="lbl"><h3>Lorem Ipsum Is Simply Dummy Text Of The Printing</h3><span>READ MORE ⟶</span></div>
  </div>
  <div class="abs sq" style="left:102px;top:355px"><svg width="12" height="12" viewBox="0 0 12 12"><path d="M8 1L3 6l5 5" stroke="#333" stroke-width="1.6" fill="none"/></svg></div>
  <div class="abs sq" style="left:1062px;top:355px"><svg width="12" height="12" viewBox="0 0 12 12"><path d="M4 1l5 5-5 5" stroke="#333" stroke-width="1.6" fill="none"/></svg></div>
</section>

<section class="abs testi">
  <div class="abs eyebrow">Real Impact</div>
  <h2 class="abs">Our Testmonials</h2>
  <div class="abs divider"></div>
  <p class="abs lead">Lorem Ipsum is simply dummy text of the printing and typesetting industry. Lorem Ipsum has been the industry's standard</p>
  <div class="abs tc blue" style="left:125px">
    <span class="q">”</span>
    Lorem Ipsum is simply dummy text of the printing and typesetting industry. Lorem Ipsum has been the industry' s standard dummy text ever sinc
    <span class="who">Maya &amp; Leo</span>
    <span class="av" role="img" aria-label="Portrait of a smiling woman" style="background:linear-gradient(135deg,#c44a2a,#5a2a20)"></span>
  </div>
  <div class="abs tc white" style="left:583px">
    <span class="q">”</span>
    Lorem Ipsum is simply dummy text of the printing and typesetting industry. Lorem Ipsum has been the industry' s standard dummy text ever sinc
    <span class="who">Sam &amp; Priya</span>
    <span class="av" role="img" aria-label="Portrait of a man in a yellow shirt" style="background:linear-gradient(135deg,#f2b632,#8a5a1e)"></span>
  </div>
  <div class="abs tc white" style="left:1064px;width:136px;padding:56px 0 0 50px">
    <span style="display:block;width:86px;overflow:hidden;white-space:nowrap">Lorem Ipsum<br>typesetting in<br>standard dum</span>
    <span class="av" role="img" aria-label="Portrait of an older man" style="left:52px;background:linear-gradient(135deg,#d8d2c8,#7a7066)"></span>
  </div>
  <div class="abs ring" style="left:125px;top:551px;border:2px solid var(--blue)"><svg width="14" height="14" viewBox="0 0 14 14"><path d="M9 2L4 7l5 5" stroke="#22409a" stroke-width="2" fill="none"/></svg></div>
  <div class="abs ring" style="left:177px;top:551px;background:var(--navy)"><svg width="14" height="14" viewBox="0 0 14 14"><path d="M5 2l5 5-5 5" stroke="#fff" stroke-width="2" fill="none"/></svg></div>
</section>

<footer class="abs footer"></footer>
<div class="abs news">
  <small>Newsletter Signup</small>
  <h2>Subscribe Our<br>Newsletter</h2>
  <div class="field" style="top:78px">Name</div>
  <div class="field" style="top:136px">Email<span class="send"><svg width="18" height="18" viewBox="0 0 18 18"><path d="M2 9l14-7-5 14-2-6z" fill="#fff"/></svg></span></div>
</div>
<div class="abs foot-brand"><span class="dot"></span>HALIF, Inc.</div>
<div class="abs socials" aria-label="Social media links"><span></span><span></span><span></span><span></span><span></span></div>
<nav class="abs foot-nav"><span>Home</span><span>Services</span><span>Administration</span><span>School Readiness</span><span>Employment</span><span>About Us</span><span>PFR - Apply Now</span></nav>
<div class="abs copy">© Copyright 2023 <b>Brightwave Studio</b> . All Rights Reserved</div>

</body>
</html>
```